Board to put on a meditation centre - Lantern Hill Haven

I need a board design for a new meditation centre based in Oslo which offers free courses in meditation and self-empowerment. The size of the board is width 374cm x height 104cm.  The name of the meditation centre together with subtitles should be on the board but also some elegant decoration that matches the theme (lantern hill haven/meditation).
Here is the website of the meditation centre to give you a feeling of it: https://lyktebakkenkurs.no/
Good if you can use a blue color close to this one: rgb(37, 180, 193) as well as some brown/golden color (similar to the palette on the website).
On the board it should say:
Lyktebakken senter (in big letters, the rest is subtitles)
Meditasjon & Spirituell visdom
Kurs - Retreat - Dialog
lyktebakkenkurs.no
The design should be very elegant and beautiful and the feeling should be of "An Lantern Hill Haven". A logo is here attached and should be used but I need to get a better quality version of it, will upload that as soon as possible.

```html
<!DOCTYPE html>
<html lang="no">
<head>
<meta charset="utf-8">
<title>Lyktebakken senter – skilt</title>
<link rel="stylesheet" href="https://fonts.googleapis.com/css2?family=Playfair+Display:wght@500&family=Josefin+Sans:wght@400;600&display=swap">
<style>
  :root {
    --backdrop: #474747;
    --paper: #f3f4f3;
    --ink: #0d0d0d;
    --aqua: #9aeef8;
    --aqua-soft: rgba(154, 238, 248, 0);
    --lagoon-deep: #1d4a40;
    --lagoon: #2f6a5b;
    --sand: #d9c3a6;
    --shore-green: #5b6e3c;
    --white: #ffffff;
  }
  * { margin: 0; padding: 0; box-sizing: border-box; }
  html, body { width: 1200px; height: 438px; overflow: hidden; background: var(--backdrop); }
  .board {
    position: absolute; left: 0; top: 52px;
    width: 1200px; height: 333px;
    background: var(--paper);
    overflow: hidden;
  }
  .decor { position: absolute; inset: 0; width: 100%; height: 100%; }
  .brand {
    position: absolute; left: 24px; top: 30px;
    display: flex; align-items: center; gap: 8px;
    font-family: "Josefin Sans", sans-serif; font-weight: 600;
    font-size: 13px; letter-spacing: 1px; color: var(--ink);
  }
  .brand-dot { width: 14px; height: 14px; border-radius: 50%; background: var(--ink); }
  .title {
    position: absolute; left: 22px; top: 96px;
    font-family: "Playfair Display", serif; font-weight: 500;
    font-size: 58px; line-height: 1; letter-spacing: 0.5px;
    color: var(--ink); white-space: nowrap;
  }
  .subtitle-band {
    position: absolute; left: 0; top: 187px;
    width: 560px; height: 62px;
    background: linear-gradient(90deg, var(--aqua) 0%, var(--aqua) 55%, var(--aqua-soft) 100%);
  }
  .subtitle {
    position: absolute; left: 24px; top: 196px;
    font-family: "Josefin Sans", sans-serif; font-weight: 600;
    font-size: 20px; line-height: 25px; letter-spacing: 1.2px;
    color: var(--ink); text-transform: uppercase;
  }
  .web {
    position: absolute; left: 24px; top: 307px;
    display: flex; align-items: center; gap: 7px;
    font-family: "Josefin Sans", sans-serif; font-weight: 600;
    font-size: 10px; letter-spacing: 5px; color: var(--ink); text-transform: uppercase;
  }
</style>
</head>
<body>
  <main class="board">
    <svg class="decor" viewBox="0 0 1200 333" aria-hidden="false">
      <defs>
        <linearGradient id="lagoon-fill" x1="0" y1="0" x2="1" y2="1">
          <stop offset="0" stop-color="var(--lagoon)"/>
          <stop offset="0.55" stop-color="var(--lagoon-deep)"/>
          <stop offset="0.8" stop-color="var(--sand)"/>
          <stop offset="1" stop-color="var(--shore-green)"/>
        </linearGradient>
      </defs>
      <path class="splash" fill="var(--aqua)"
        d="M660 0 L800 0 L770 40 L740 90 L720 150 L700 175 L690 160 L700 120 L680 110 L690 80 L670 60 L680 30 Z"/>
      <path class="shore-photo" role="img" aria-label="Luftfoto av en rolig lagune med sandstrand, holmer og små båter"
        fill="url(#lagoon-fill)"
        d="M790 0 L1200 0 L1200 333 L870 333 L840 310 L800 300 L780 280 L750 270 L730 245 L745 215 L725 190 L735 165 L715 150 L735 120 L750 90 L770 50 Z"/>
      <g class="rings" fill="none">
        <circle cx="188" cy="8" r="44" stroke="var(--aqua)" stroke-width="4"/>
        <circle cx="501" cy="268" r="16" stroke="var(--aqua)" stroke-width="7"/>
        <circle cx="436" cy="330" r="44" stroke="var(--aqua)" stroke-width="5"/>
        <circle cx="964" cy="8" r="12" stroke="var(--white)" stroke-width="5"/>
        <circle cx="1153" cy="115" r="42" stroke="var(--white)" stroke-width="8"/>
        <circle cx="1099" cy="172" r="11" stroke="var(--white)" stroke-width="5"/>
      </g>
    </svg>

    <div class="brand"><span class="brand-dot"></span>Lyktebakken senter</div>

    <h1 class="title">LYKTEBAKKEN SENTER</h1>

    <div class="subtitle-band"></div>
    <p class="subtitle">Meditasjon &amp; Spirituell visdom<br>Kurs - Retreat - Dialog</p>

    <p class="web">
      <svg width="9" height="9" viewBox="0 0 10 10" aria-hidden="true">
        <circle cx="5" cy="5" r="4.3" fill="none" stroke="var(--ink)" stroke-width="1.2"/>
        <path d="M0.7 5 H9.3 M5 0.7 C2.5 3 2.5 7 5 9.3 M5 0.7 C7.5 3 7.5 7 5 9.3" fill="none" stroke="var(--ink)" stroke-width="0.9"/>
      </svg>
      lyktebakkenkurs.no
    </p>
  </main>
</body>
</html>
```